coaching agenda

Please redesign the brochure attached in a more modern/trendy out look. I want something completely different to what is attached but using the same colours and logo.

```html
<!DOCTYPE html>
<html lang="en">
<head>
<meta charset="utf-8">
<title>Coaching Session – June 2018</title>
<link href="https://fonts.googleapis.com/css2?family=Crimson+Text:wght@400;600;700&family=Cormorant+Garamond:wght@400;500&family=Open+Sans:wght@400;600&display=swap" rel="stylesheet">
<style>
:root{
  --brand-blue:#1b9fd3;
  --navy:#1d2a44;
  --ink:#2b2b2b;
  --panel-dark:#2e2e2e;
  --panel-mid:#5a5a5a;
  --paper:#ffffff;
  --paper-grey:#e9eaeb;
  --stage:#d9dadc;
  --heading-blue:#1d7fb8;
}
*{box-sizing:border-box;margin:0;padding:0}
html,body{width:1200px;height:800px;overflow:hidden}
body{background:var(--stage);font-family:"Crimson Text",Georgia,serif;color:var(--ink);position:relative}
.page{position:absolute;top:32px;width:520px;height:736px;background:var(--paper);overflow:hidden;box-shadow:0 2px 10px rgba(0,0,0,.18)}
.page--agenda{left:40px}
.page--cover{left:640px}
.photo{position:absolute;left:0;top:0;width:100%}
.page--agenda .photo{height:300px;background:linear-gradient(135deg,#0f1a2e 0%,#25344f 45%,#6b7078 75%,#2a3347 100%)}
.page--cover .photo{height:330px;background:linear-gradient(160deg,#6e6f72 0%,#3a3b3e 35%,#8a8b8e 60%,#55565a 100%)}
.intro-panel{position:absolute;left:34px;top:26px;width:232px;height:254px;background:rgba(95,95,98,.78);color:#fff;padding:20px 18px;font-size:11.5px;font-weight:600;line-height:1.3}
.intro-panel p{margin-bottom:12px}
.agenda-body{position:absolute;left:26px;right:22px;top:316px;bottom:48px;display:flex;gap:18px;font-size:7px;line-height:1.22}
.agenda-col{flex:1}
.agenda-col ol{padding-left:12px}
.agenda-col ul{padding-left:12px;list-style:"· "}
.agenda-col em{font-weight:700;font-style:italic}
.footer{position:absolute;left:0;right:0;bottom:0;height:40px;background:var(--brand-blue);color:#fff;font-family:"Open Sans",Arial,sans-serif;font-size:10px;display:flex;align-items:center;padding-left:40px;gap:8px}
.footer b{font-weight:600}
.logo-box{position:absolute;top:0;right:22px;width:168px;height:138px;background:var(--paper);display:flex;flex-direction:column;align-items:center;justify-content:center;gap:6px;color:var(--navy)}
.logo-mark{width:34px;height:34px;background:var(--brand-blue)}
.logo-name{font-size:19px;font-weight:600;color:var(--navy)}
.logo-sub{font-size:7px;font-weight:600;color:var(--navy);margin-top:-6px}
.cover-title{position:absolute;left:26px;top:238px;color:#fff;font-family:"Cormorant Garamond",Georgia,serif;font-variant:small-caps;font-size:31px;font-weight:500;line-height:.9;letter-spacing:.5px}
.lower{position:absolute;left:0;right:0;top:330px;bottom:40px;background:linear-gradient(180deg,#f4f4f5 0%,var(--paper-grey) 100%)}
.questions{position:absolute;left:42px;top:18px;width:226px;height:250px;background:linear-gradient(180deg,#3a3a3a 0%,var(--panel-dark) 40%,var(--panel-mid) 100%);color:#fff;padding:26px 16px;font-size:10px;font-weight:600;line-height:1.25}
.questions h3{font-size:11px;font-weight:600;margin-bottom:18px}
.questions p{margin-bottom:20px}
.gets{position:absolute;left:288px;top:18px;width:210px;font-size:6.5px;line-height:1.25}
.gets h2{color:var(--heading-blue);font-size:10px;font-weight:700;margin-bottom:10px}
.gets ol{padding-left:12px}
</style>
</head>
<body>

<section class="page page--agenda">
  <div class="photo" role="img" aria-label="Photo of a businessman's clasped hands resting on a meeting table"></div>
  <div class="intro-panel">
    <p>Today onwards [12/6/18]<br>Build the listing pipeline so you have shock coming to market when the sun shines again.</p>
    <p>Don't wait until the usual "spring selling session" promo's start to start looking for listings.</p>
    <p>Get the jump on your competition by having your July to December profile building campaign set in place now &amp; make sure it is fully funded so you don't lose profile momentum.</p>
  </div>
  <div class="agenda-body">
    <div class="agenda-col">
      <ol>
        <li>What went well this month?</li>
        <li>Did you convert good days into good weeks, good weeks into a good month?</li>
        <li>How organised were you last week?</li>
        <li>What ideas, actions, processes, systems and motivations have you introduced into your business during the last thirty days?</li>
        <li>What systems do you need to implement to create a smoother work flow?</li>
        <li>Are you pursuing what you believe in?</li>
        <li>At what time of the day are you running at your true potential?</li>
        <li>What have been your numbers for May?
          <ul>
            <li>Speaker's</li><li>Appointments</li><li>Appraisals</li><li>Listing presentations</li><li>Listing pipeline</li><li>Listing authorities signed</li><li>Listings launched</li><li>Home opens</li><li>Negotiations</li><li>Sales</li><li>Lessons learned list</li>
            <li>Inroads into the market share in your core area – are you competitive, you when you are being called in</li>
          </ul>
        </li>
        <li>Script session – what was the best script you used last week?</li>
        <li>Stock review</li>
        <li>Build an audience<br>All real estate sales people have customers. Lucky ones have fans. But the most fortunate real estate sales people have <em>audiences.</em><br>An audience can be your point of difference. A lot of real estate people still spend big bucks to reach people. Every time they want to say something, they dip into their marketing budgets, pull out some cash and do some "marketing". This approach is both expensive and unreliable. As has been said, you waste half of your marketing budget, you just don't know which half.<br>Today's smart real estate sales person knows better. Instead of going out to reach people, you want people to come to you. An <em>audience</em> returns often – on its own – to see what you have to say.</li>
      </ol>
    </div>
    <div class="agenda-col">
      <p>This is the most receptive group of prospective customers and customers you'll ever have.</p>
      <ul>
        <li>Send</li><li>Say</li><li>Connect</li><li>Capture</li><li>Connect</li><li>Present</li><li>Convert</li><li>List</li><li>Market</li><li>Sell</li><li>Retain</li>
      </ul>
      <ol start="12">
        <li>Make the uncommon common
          <ul>
            <li>Time – no time is no excuse – you cannot be defined by time in 2018 / the need to do more for less following the industry discounting of fees.</li>
            <li>How you manage free time</li>
            <li>You cannot be defined by not knowing what to do</li>
            <li>Embrace where your market is at:
              <ul><li>2015 – Wow</li><li>2016 – Hope</li><li>2017 – New norm</li><li>2018 – The norm</li></ul>
            </li>
          </ul>
          What are your behaviours costing you
          <ul>
            <li>Public domain – those areas where people see you acting on your behaviours, both positive &amp; negative. Professionalism, application, integrity, self-esteem, respect for others &amp; proficiency are on display here</li>
            <li>Private domain – is the one where we spend time with ourselves &amp; where our mind games play out. This is the biggest behavioural game of all as we confront our habits, limitations, acceptance of disruptions, temptations &amp; fears</li>
            <li>Know your CRM system</li>
            <li>Capture data &amp; use it to generate an income</li>
            <li>Buyer work</li>
            <li>6 weeks after settlement</li>
            <li>Significantly increase the number of "just listed" you drop</li>
            <li>Put a name to a property</li>
          </ul>
        </li>
      </ol>
    </div>
  </div>
  <footer class="footer"><b>E:</b> coach@hartsalescoach.com.au &nbsp;|&nbsp; <b>P:</b> +61 400 512 870 &nbsp;|&nbsp; <b>M:</b> PO Box 4410, Riverside WA 6050</footer>
</section>

<section class="page page--cover">
  <div class="photo" role="img" aria-label="Photo of businesspeople's legs in dark suits and shoes walking across a carpeted office"></div>
  <div class="logo-box">
    <div class="logo-mark"></div>
    <div class="logo-name">Daniel Hart</div>
    <div class="logo-sub">Sales Coaching (Australia) Pty Ltd</div>
  </div>
  <h1 class="cover-title">Coaching Session<br>June 2018</h1>
  <div class="lower">
    <div class="questions">
      <h3>Yesterday – Today – Tomorrow</h3>
      <p>How many appraisals/listing presentations are booked in your diary for this week?</p>
      <p>How many appraisals/listing presentations are booked in your diary for next week?</p>
      <p>How many second viewings/private viewings are booked in your diary for this week?</p>
      <p>How many listings will you launch this week?</p>
    </div>
    <div class="gets">
      <h2>2018/2019 Productivity Gets</h2>
      <p>There's more to it than numbers:</p>
      <ol>
        <li>Increase in market share in your core area</li>
        <li>Increase in commission rates</li>
        <li>Relationships [data base growth] – future sellers</li>
        <li>Relationships [data base growth] – buyer prospects</li>
        <li>Number of appointments/appraisals booked each week</li>
        <li>Listing pipeline growth</li>
        <li>Skills development – is an opportunity – you can't be defined as not knowing what to do. Be specific. You can't become a better closer if you don't have people to close on!!</li>
        <li>Managing free time – you can't be defined by time</li>
        <li>Time is an opportunity</li>
        <li>Know your data base system – data base is an opportunity</li>
        <li>Service charter – there is opportunity in service – repeat/referrals/the future seller calls "you in"</li>
        <li>Health &amp; energy leads to better recovery</li>
        <li>Family &amp; self-breaks</li>
        <li>Self-time</li>
        <li>Milestones/benchmarks</li>
        <li>Wealth creation</li>
      </ol>
    </div>
  </div>
  <footer class="footer"><b>E:</b> coach@hartsalescoach.com.au &nbsp;|&nbsp; <b>P:</b> +61 400 512 870 &nbsp;|&nbsp; <b>M:</b> PO Box 4410, Riverside WA 6050</footer>
</section>

</body>
</html>
```